Business Card Design

Selling beds and mattrices
See website www.lunorest.com.au for details
Targeting wholesale bed sellers

Industry/Entity Type

Business

Contact Information for Business Card

Lunorest
Director Gerald Whitcombe
Beds and Mattrices - Most technologically advanced beds in the world
European designed and made
Already No 1 seller in Europe
Call now for a quote
ph: 0472 518 306
Email: sales@lunorest.com.au
www.lunorest.com.au

```html
<!DOCTYPE html>
<html lang="en">
<head>
<meta charset="utf-8">
<title>Lunorest Business Card</title>
<link href="https://fonts.googleapis.com/css2?family=Open+Sans:wght@400;600;700&display=swap" rel="stylesheet">
<style>
  :root {
    --bg: #e9e7e4;
    --card: #ffffff;
    --ink: #1c1c1c;
    --ink-soft: #3a3a3a;
    --rule: #2a2a2a;
    --photo-light: #eef0f4;
    --photo-mid: #b9b7c4;
    --photo-lilac: #9a8fb0;
    --photo-warm: #c9a27a;
    --photo-dark: #4b4e58;
  }
  * { box-sizing: border-box; margin: 0; padding: 0; }
  html, body { width: 1200px; height: 803px; overflow: hidden; }
  body {
    background: var(--bg);
    font-family: "Open Sans", Arial, sans-serif;
    color: var(--ink);
    position: relative;
  }
  .card {
    position: absolute;
    top: 251px;
    width: 540px;
    height: 300px;
    background: var(--card);
    box-shadow: 0 6px 20px rgba(0,0,0,0.18);
    overflow: hidden;
  }
  .card--front { left: 40px; }
  .card--back { left: 620px; }

  /* front */
  .bedroom-photo {
    position: absolute; inset: 0;
    background:
      radial-gradient(ellipse at 35% 55%, var(--photo-light) 0%, rgba(238,240,244,0) 55%),
      linear-gradient(160deg, var(--photo-lilac) 0%, var(--photo-mid) 30%, var(--photo-light) 55%, var(--photo-warm) 78%, var(--photo-dark) 100%);
  }
  .brand-name {
    font-weight: 600;
    color: var(--ink);
    line-height: 1;
  }
  .front-brand {
    position: absolute;
    left: 50%; top: 50%;
    transform: translate(-50%, -50%);
    font-size: 44px;
  }

  /* back */
  .back-inner {
    position: absolute; inset: 26px 28px 28px;
    display: flex; flex-direction: column; justify-content: space-between;
  }
  .back-head { display: flex; justify-content: space-between; align-items: flex-start; }
  .back-brand .brand-name { font-size: 30px; }
  .product-line {
    margin-top: 14px;
    font-size: 12px; font-weight: 400; letter-spacing: 9px;
    text-transform: uppercase;
  }
  .person { text-align: right; }
  .person-name { font-size: 17px; font-weight: 700; }
  .person-role { font-size: 9px; letter-spacing: 1px; text-transform: uppercase; color: var(--ink-soft); }
  .rule { border: 0; border-top: 1px solid var(--rule); }
  .claims {
    text-align: center; text-transform: uppercase;
    font-size: 10.5px; line-height: 1.8; letter-spacing: 0.3px;
  }
  .claims .cta { font-weight: 700; font-size: 11.5px; }
  .claims .cta-label { font-weight: 400; }
  .contacts { display: flex; justify-content: space-between; font-size: 12.5px; font-weight: 700; }
  .contact { display: flex; align-items: center; gap: 6px; }
  .contact svg { width: 16px; height: 16px; }
</style>
</head>
<body>
  <section class="card card--front">
    <div class="bedroom-photo" role="img" aria-label="Photograph of a bright modern bedroom with a white bed"></div>
    <div class="front-brand brand-name">Lunorest</div>
  </section>

  <section class="card card--back">
    <div class="back-inner">
      <div class="back-head">
        <div class="back-brand">
          <div class="brand-name">Lunorest</div>
          <div class="product-line">Beds &amp; Mattrices</div>
        </div>
        <div class="person">
          <div class="person-name">Gerald Whitcombe</div>
          <div class="person-role">Director</div>
        </div>
      </div>
      <hr class="rule">
      <div class="claims">
        <p>Most technologically advanced beds in the world</p>
        <p>European designed and made already No 1 seller in Europe</p>
        <p class="cta">Call now for a quote <span class="cta-label">phone</span> 0472 518 306</p>
      </div>
      <hr class="rule">
      <div class="contacts">
        <div class="contact">
          <svg viewBox="0 0 16 16" aria-hidden="true"><circle cx="8" cy="8" r="8" fill="#1c1c1c"/><rect x="4" y="5" width="8" height="6" fill="none" stroke="#fff" stroke-width="1"/><path d="M4 5 L8 8.5 L12 5" fill="none" stroke="#fff" stroke-width="1"/></svg>
          sales@lunorest.com.au
        </div>
        <div class="contact">
          <svg viewBox="0 0 16 16" aria-hidden="true"><circle cx="8" cy="8" r="8" fill="#1c1c1c"/><circle cx="8" cy="8" r="4" fill="none" stroke="#fff" stroke-width="1"/><path d="M4 8 H12 M8 4 C6 6 6 10 8 12 M8 4 C10 6 10 10 8 12" fill="none" stroke="#fff" stroke-width="0.8"/></svg>
          www.lunorest.com.au
        </div>
      </div>
    </div>
  </section>
</body>
</html>
```